Mobile Friendly Lead Generation Landing Page

We are a web marketing company that specialized in web lead generation. Recently we have started buying media from mobile devices and we need a mobile interface(landing page) where we can collect user data in an effective manner.

Our current mobile landing page is:
http://www.tuitionscout.example.com/lp13d/index.aspx?a=true&source=581406
Through this you can see what the steps/questions users need to answer to get matched to a school. We need the design for the whole process.

We are pretty open for design ideas and our goal is to make this mobile optimized landing page have the look and feel of an app...but not an app.
There are several questions in the process but we are open to changing the way they are presented. As in, you can have one question at a time or a few.
The goal is to make this EXTREMELY EASY for users to interact with.

One example that we have liked is:
http://lessonhub.example/schools/47215-page1.lhub (please note that this opens only on mobile devices)

Some of these screenshots are attached.

Our web form looks like this:
http://www.tuitionscout.example.com/lp88/index.aspx?a=true

```html
<!DOCTYPE html>
<html lang="en">
<head>
<meta charset="utf-8">
<title>School Match – Step Form</title>
<link rel="stylesheet" href="https://fonts.googleapis.com/css2?family=Open+Sans:wght@300;400;600;700&display=swap">
<style>
  :root{
    --status-bg:#2f3742;
    --header-bg:#3f5066;
    --header-bg-2:#465a70;
    --progress-bg:#26303e;
    --track:#3b4b5e;
    --fill:#2f9a2a;
    --fill-light:#7bc94a;
    --body-bg:#e9e9e9;
    --card:#ffffff;
    --ink:#6b6b6b;
    --ink-soft:#7b8796;
    --white:#ffffff;
    --go:#80c84f;
    --tick:#6cc04a;
    --cross:#ef5a5a;
    --chip:#e8e8e8;
    --badge:#c9d3de;
    --badge-2:#e5e9ee;
    --brand:#27466e;
  }
  *{margin:0;padding:0;box-sizing:border-box}
  html,body{width:1200px;height:2185px;overflow:hidden}
  body{font-family:"Open Sans",Arial,sans-serif;background:var(--body-bg);position:relative;color:var(--ink)}

  .status-bar{position:absolute;left:0;top:0;width:1200px;height:65px;background:var(--status-bg);color:#e6e6e6;font-weight:600;font-size:40px}
  .status-bar .carrier{position:absolute;left:22px;top:4px;display:flex;align-items:center;gap:10px}
  .status-bar .time{position:absolute;left:0;width:1200px;top:4px;text-align:center}
  .status-bar .battery{position:absolute;right:20px;top:4px;display:flex;align-items:center;gap:12px}

  .app-header{position:absolute;left:0;top:65px;width:1200px;height:173px;background:linear-gradient(90deg,var(--header-bg),var(--header-bg-2))}
  .app-header .title{position:absolute;left:0;width:1200px;top:54px;text-align:center;color:var(--white);font-size:43px;font-weight:400}
  .app-header .title strong{font-weight:700}
  .app-header .nav{position:absolute;top:53px}
  .nav.prev{left:80px}
  .nav.next{right:80px}

  .progress{position:absolute;left:0;top:238px;width:1200px;height:324px;background:var(--progress-bg)}
  .progress .seg{position:absolute;top:108px;height:60px;background:var(--track)}
  .seg.one{left:151px;width:197px;background:repeating-linear-gradient(120deg,var(--fill) 0 8px,#2a8a26 8px 14px)}
  .seg.two{left:367px;width:430px}
  .seg.two .done{position:absolute;left:0;top:0;height:60px;width:156px;background:repeating-linear-gradient(120deg,var(--fill-light) 0 8px,#6dba3f 8px 14px)}
  .seg.three{left:811px;width:255px}
  .progress .label{position:absolute;left:0;width:1200px;top:194px;text-align:center;color:var(--ink-soft);font-size:26px;font-weight:300}

  .question-card{position:absolute;left:53px;top:619px;width:1097px;height:1054px;background:var(--card);box-shadow:0 3px 4px rgba(0,0,0,.08)}
  .question-card h1{position:absolute;left:0;width:100%;top:66px;text-align:center;font-size:53px;font-weight:300;color:var(--ink)}
  .option{position:absolute;left:384px;display:flex;align-items:center;gap:44px;font-size:55px;font-weight:300;color:var(--ink)}
  .option.yes{top:320px}
  .option.no{top:529px}
  .option .mark{width:96px;height:96px;border-radius:50%;background:var(--chip);box-shadow:inset 0 -3px 0 rgba(0,0,0,.06);display:flex;align-items:center;justify-content:center}
  .next-button{position:absolute;left:89px;top:816px;width:895px;height:147px;background:var(--go);border-radius:6px;color:var(--white);font-size:57px;font-weight:700;display:flex;align-items:center;justify-content:center;gap:70px}

  .trust-strip{position:absolute;left:50px;top:1757px;width:1092px;height:249px;background:var(--card);box-shadow:0 3px 4px rgba(0,0,0,.08)}
  .brand{position:absolute;left:80px;top:94px;display:flex;align-items:center;gap:14px;font-size:40px;font-weight:600;color:var(--brand)}
  .brand .dot{width:40px;height:40px;border-radius:50%;background:var(--brand)}
  .badge{position:absolute}
  .badge.secure{left:437px;top:60px;width:230px;height:130px;background:var(--badge-2);border-radius:6px}
  .badge.rated{left:840px;top:70px;width:180px;height:110px;background:var(--badge);border-radius:4px}
</style>
</head>
<body>
  <div class="status-bar">
    <div class="carrier">
      <svg width="70" height="30" viewBox="0 0 70 30"><g fill="#e6e6e6"><rect x="0" y="20" width="10" height="10"/><rect x="14" y="15" width="10" height="15"/><rect x="28" y="10" width="10" height="20"/><rect x="42" y="5" width="10" height="25"/><rect x="56" y="0" width="10" height="30"/></g></svg>
      <span>VELA</span>
    </div>
    <div class="time">10:35 AM</div>
    <div class="battery">
      <svg width="36" height="36" viewBox="0 0 36 36"><circle cx="18" cy="18" r="16" fill="#e6e6e6"/><path d="M18 8v11h8" stroke="#2f3742" stroke-width="4" fill="none"/></svg>
      <span>65%</span>
      <svg width="80" height="36" viewBox="0 0 80 36"><rect x="2" y="2" width="68" height="32" rx="3" fill="none" stroke="#e6e6e6" stroke-width="3"/><rect x="7" y="7" width="40" height="22" fill="#e6e6e6"/><rect x="72" y="12" width="6" height="12" fill="#e6e6e6"/></svg>
    </div>
  </div>

  <header class="app-header">
    <svg class="nav prev" width="64" height="64" viewBox="0 0 64 64"><circle cx="32" cy="32" r="29" fill="none" stroke="#8c9aab" stroke-width="4"/><path d="M46 32H20M30 21 19 32l11 11" fill="none" stroke="#8c9aab" stroke-width="4" stroke-linecap="round" stroke-linejoin="round"/></svg>
    <div class="title">Fill out our <strong>3 minute</strong> form!</div>
    <svg class="nav next" width="64" height="64" viewBox="0 0 64 64"><circle cx="32" cy="32" r="29" fill="none" stroke="#8c9aab" stroke-width="4"/><path d="M18 32h26M34 21l11 11-11 11" fill="none" stroke="#8c9aab" stroke-width="4" stroke-linecap="round" stroke-linejoin="round"/></svg>
  </header>

  <section class="progress">
    <div class="seg one"></div>
    <div class="seg two"><div class="done"></div></div>
    <div class="seg three"></div>
    <div class="label">progress : 76% completed</div>
  </section>

  <main class="question-card">
    <h1>Are you currently in school?</h1>
    <div class="option yes">
      <span class="mark"><svg width="50" height="40" viewBox="0 0 50 40"><path d="M5 21l13 13L45 6" fill="none" stroke="var(--tick)" stroke-width="7" stroke-linecap="round" stroke-linejoin="round"/></svg></span>
      <span>Yes</span>
    </div>
    <div class="option no">
      <span class="mark"><svg width="44" height="44" viewBox="0 0 44 44"><path d="M6 6l32 32M38 6 6 38" fill="none" stroke="var(--cross)" stroke-width="7" stroke-linecap="round"/></svg></span>
      <span>No</span>
    </div>
    <div class="next-button">
      <span>Next</span>
      <svg width="34" height="56" viewBox="0 0 34 56"><path d="M6 6l22 22L6 50" fill="none" stroke="#fff" stroke-width="7" stroke-linecap="round" stroke-linejoin="round"/></svg>
    </div>
  </main>

  <footer class="trust-strip">
    <div class="brand"><span class="dot"></span><span>LessonHub</span></div>
    <div class="badge secure" role="img" aria-label="Security certificate badge"></div>
    <div class="badge rated" role="img" aria-label="Accredited business rating badge"></div>
  </footer>
</body>
</html>
```